Recruitment Flyer for Harbourline Home Loan company

Harbourline Home Loan centre requires a four page A4 color brochure for new staff who will be joining the organisation.

The brochure is received during the interview for the job role. so we are looking for nice glossy pictures combined with sufficient text to enable the applicant to make an informed decision.

I have attached a word document that may help plus lots of pictures that are on the website that could be used also.

Target Market(s)

New staff joining the organisation

Industry/Entity Type

Mortgage

Font styles to use
Sans Serif

Colors
3377b5
6b449b
b768aa
34a6d7

Requirements
Must have
• Glossy, colorful and career happy
Nice to have
• lots of photos and opportunity for text
Should not have
• be sad or not happy

```html
<!DOCTYPE html>
<html lang="en">
<head>
<meta charset="utf-8">
<title>Harbourline Home Loan Centre – Brochure</title>
<link href="https://fonts.googleapis.com/css2?family=Lato:ital,wght@0,400;0,700;1,400&family=Ubuntu:wght@300;500;700&family=Courgette&display=swap" rel="stylesheet">
<style>
:root{
  --cyan:#2fbbe8;
  --cyan-deep:#34a6d7;
  --blue:#3377b5;
  --purple:#6b449b;
  --purple-deep:#5a2d96;
  --pink:#b768aa;
  --ink:#2b2b33;
  --paper:#ffffff;
  --backdrop:#e4e5e8;
}
*{box-sizing:border-box;margin:0;padding:0}
html,body{width:1200px;height:998px;overflow:hidden}
body{background:var(--backdrop);font-family:"Lato",sans-serif;color:var(--ink);position:relative}
.spread{position:absolute;width:664px;height:470px;display:flex;box-shadow:0 6px 18px rgba(0,0,0,.18)}
.spread--outer{left:60px;top:20px}
.spread--inner{left:476px;top:508px}
.page{position:relative;width:332px;height:470px;background:var(--paper);overflow:hidden}
.page>svg.bg{position:absolute;inset:0;width:100%;height:100%}
.abs{position:absolute}
.brand{display:flex;align-items:center;gap:6px;position:absolute}
.brand__dot{width:22px;height:22px;border-radius:50%;background:var(--purple)}
.brand__name{font-family:"Lato",sans-serif;font-weight:700;color:var(--cyan-deep);font-size:15px;letter-spacing:.5px;line-height:1.05}
/* back cover */
.contact{left:70px;top:205px;font-weight:700;font-size:13px;line-height:1.35;color:var(--ink)}
.contact .web{letter-spacing:4px;font-weight:400}
/* front cover */
.hero-title{right:24px;top:270px;text-align:right;color:#fff;font-family:"Ubuntu",sans-serif}
.hero-title .light{font-weight:300;font-size:36px;line-height:1;letter-spacing:1px}
.hero-title .bold{font-weight:500;font-size:66px;line-height:.95}
.hero-title .tag{font-family:"Lato",sans-serif;font-size:13.5px;margin-top:6px}
.hero-title .call{font-family:"Lato",sans-serif;font-size:15px;color:var(--purple-deep);font-weight:700;margin-top:2px}
.front-web{left:0;right:0;top:440px;text-align:center;font-size:13px;letter-spacing:4px;font-weight:700}
/* inner left */
.intro{left:26px;top:96px;width:285px;font-size:7.2px;line-height:1.35}
.points{left:26px;top:124px;width:290px;list-style:none}
.points li{position:relative;padding-left:12px;margin-bottom:9px;font-size:7.2px;line-height:1.35}
.points li::before{content:"";position:absolute;left:0;top:9px;width:4px;height:4px;border-radius:50%;background:var(--cyan-deep)}
.points h3{font-family:"Courgette",cursive;font-weight:400;color:var(--pink);font-size:10.5px;line-height:1.2}
.about-label{left:20px;top:298px;background:var(--cyan);color:var(--purple-deep);font-family:"Ubuntu",sans-serif;font-weight:700;font-size:12px;padding:2px 16px 2px 8px}
.about-text{left:26px;top:320px;width:280px;font-size:7.4px;line-height:1.35}
.about-text--narrow{top:372px;width:150px}
/* inner right */
.panel-head{left:22px;top:30px;color:#fff;font-family:"Ubuntu",sans-serif;font-weight:500;font-size:15px}
.panel-text{left:22px;top:52px;width:292px;color:#fff;font-size:6.8px;line-height:1.35}
.panel-text p{margin-bottom:6px}
.right-web{right:22px;top:440px;color:var(--purple-deep);font-weight:700;font-size:10px;letter-spacing:3px}
</style>
</head>
<body>

<section class="spread spread--outer">
  <article class="page page--back">
    <svg class="bg" viewBox="0 0 332 470" aria-hidden="true">
      <rect x="0" y="0" width="332" height="10" fill="var(--cyan)"/>
      <path d="M120,470 C190,430 260,400 332,384 L332,470 Z" fill="var(--cyan)"/>
      <path d="M95,470 C170,420 250,385 332,366 L332,384 C260,400 190,430 120,470 Z" fill="var(--purple)"/>
      <path d="M82,470 C160,415 245,378 332,356 L332,366 C250,385 170,420 95,470 Z" fill="var(--pink)"/>
    </svg>
    <div class="brand" style="left:62px;top:160px">
      <span class="brand__dot"></span>
      <span class="brand__name">Harbourline<br>Home Loan Centre</span>
    </div>
    <div class="contact abs">
      CALL US: 123 456 7890<br>
      lorem@lorem ipsum<br>
      <span class="web">www.lorem.com</span>
    </div>
  </article>

  <article class="page page--front">
    <svg class="bg" viewBox="0 0 332 470">
      <defs>
        <linearGradient id="familyTone" x1="0" y1="0" x2="1" y2="1">
          <stop offset="0" stop-color="#e9ddd0"/>
          <stop offset=".6" stop-color="#c9a98a"/>
          <stop offset="1" stop-color="#f1e9e3"/>
        </linearGradient>
        <linearGradient id="heroCyan" x1="0" y1="0" x2="1" y2="0">
          <stop offset="0" stop-color="#25b3e3"/>
          <stop offset="1" stop-color="#4dd0f3"/>
        </linearGradient>
      </defs>
      <rect x="28" y="60" width="304" height="250" fill="url(#familyTone)" role="img" aria-label="Photo of a smiling family of four unpacking moving boxes in their new home"/>
      <path d="M0,470 L0,405 C70,300 190,250 332,236 L332,425 L0,425 Z" fill="url(#heroCyan)"/>
      <path d="M0,405 C70,300 190,250 332,236" fill="none" stroke="var(--purple)" stroke-width="6"/>
      <rect x="0" y="423" width="332" height="3" fill="var(--purple)"/>
    </svg>
    <div class="brand" style="left:102px;top:20px">
      <span class="brand__dot"></span>
      <span class="brand__name">Harbourline<br>Home Loan Centre</span>
    </div>
    <div class="hero-title abs">
      <div class="light">Lorem</div>
      <div class="bold">Ipsum</div>
      <div class="tag">simply dummy text of the printing</div>
      <div class="call">CALL US: 123 456 7890</div>
    </div>
    <div class="front-web abs">www.lorem.com</div>
  </article>
</section>

<section class="spread spread--inner">
  <article class="page page--inner-left">
    <svg class="bg" viewBox="0 0 332 470">
      <rect x="0" y="0" width="332" height="8" fill="var(--pink)"/>
      <rect x="0" y="8" width="332" height="4" fill="var(--purple)"/>
      <rect x="40" y="118" width="270" height="175" fill="#f1f1f3" role="img" aria-label="Faded photo of a family relaxing together outdoors"/>
      <path d="M0,474 C130,462 250,425 336,370" fill="none" stroke="var(--purple)" stroke-width="12"/>
      <path d="M0,490 C140,480 265,445 336,392" fill="none" stroke="var(--cyan)" stroke-width="16"/>
      <circle cx="252" cy="414" r="50" fill="var(--purple)"/>
      <circle cx="252" cy="414" r="47" fill="#fff"/>
      <circle cx="252" cy="414" r="43" fill="#9aa79a" role="img" aria-label="Photo of smiling volunteers in grey T-shirts outdoors"/>
    </svg>
    <div class="brand" style="left:82px;top:38px">
      <span class="brand__dot"></span>
      <span class="brand__name">Harbourline<br>Home Loan Centre</span>
    </div>
    <p class="intro abs">Lorem Ipsum is simply dummy text of the printing and typesetting industry. Lorem Ipsum has been the industry's standard dummy text ever since the 1500s</p>
    <ul class="points abs">
      <li><h3>Looreem ipsum</h3>Contrary to popular belief, Lorem Ipsum is not simply random text. It has roots in a piece of classical Latin literature from 45 BC</li>
      <li><h3>Looreem ipsum</h3>Contrary to popular belief, Lorem Ipsum is not simply random text. It has roots in a piece of classical Latin literature from 45 BC</li>
      <li><h3>Looreem ipsum</h3>Contrary to popular belief, Lorem Ipsum is not simply random text. It has roots in a piece of classical Latin literature from 45 BC</li>
      <li><h3>Looreem ipsum</h3>Contrary to popular belief, Lorem Ipsum is not simply random text. It has roots in a piece of classical Latin literature from 45 BC</li>
    </ul>
    <div class="about-label abs">ABOUT US:</div>
    <p class="about-text abs">It is a long established fact that a reader will be distracted by the readable content of a page when looking at its layout. The point of using Lorem Ipsum is that it has a more-or-less normal distribution of letters, as opposed to using 'Content here, content here'</p>
    <p class="about-text about-text--narrow abs">Many desktop publishing packages and web page editors now use Lorem Ipsum as their default model text, and a search for 'lorem ipsum' will uncover many web sites still in their infancy.</p>
  </article>

  <article class="page page--inner-right">
    <svg class="bg" viewBox="0 0 332 470">
      <defs>
        <linearGradient id="panelCyan" x1="0" y1="0" x2="1" y2="1">
          <stop offset="0" stop-color="#2bb8e6"/>
          <stop offset="1" stop-color="#5fd6f5"/>
        </linearGradient>
        <linearGradient id="agentTone" x1="0" y1="0" x2="1" y2="0">
          <stop offset="0" stop-color="#d7b4a0"/>
          <stop offset=".55" stop-color="#eee6e2"/>
          <stop offset="1" stop-color="#cfd3d8"/>
        </linearGradient>
      </defs>
      <rect width="332" height="470" fill="url(#panelCyan)"/>
      <path d="M30,470 C60,330 180,232 332,212 L332,470 Z" fill="url(#agentTone)" role="img" aria-label="Photo of a smiling customer service agent wearing a headset, with colleagues in the background"/>
      <path d="M22,470 C52,325 175,226 332,205" fill="none" stroke="var(--purple-deep)" stroke-width="12"/>
      <path d="M14,470 C45,318 170,216 332,194" fill="none" stroke="var(--pink)" stroke-width="4"/>
    </svg>
    <h2 class="panel-head abs">Lorem Ipsum:</h2>
    <div class="panel-text abs">
      <p>There are many variations of passages of Lorem Ipsum available, but the majority have suffered alteration in some form, by injected humour, or randomised words which don't look even slightly believable. If you are going to use a passage of Lorem Ipsum</p>
      <p>There are many variations of passages of Lorem Ipsum available, but the majority have suffered alteration in some form, by injected humour, or randomised words which don't look even slightly believable. If you are going to use a passage of Lorem Ipsum</p>
      <p>There are many variations of passages of Lorem Ipsum available, but the majority have suffered alteration in some form, by injected humour, or randomised words which don't look even slightly believable. If you are going to use a passage of Lorem Ipsum</p>
      <p>Contrary to popular belief, Lorem Ipsum is not simply random text. It has roots in a piece of classical Latin literature from 45 BC</p>
    </div>
    <div class="brand" style="left:180px;top:250px">
      <span class="brand__dot"></span>
      <span class="brand__name" style="font-size:12px">Harbourline<br>Home Loan Centre</span>
    </div>
    <div class="right-web abs">www.lorem.com</div>
  </article>
</section>

</body>
</html>
```